Redstone Valley Medical Group Business sign

Business sign around 3' x 4' or 4' x 4'. Exterior sign next to busy road. Want to contrast with current signage, which will be the structure that we bolt the new sign you are designing for us here on Pixel Bazaar. Old sign is blue, but could be painted to provide different background color. The of our business is "Redstone Valley Medical Group". It is known locally as "The Wellness Lodge". I'm wondering if that could appear below the name in quotes.

Redstone Valley
Medical Group
"The Wellness Lodge"

I attached a picture of pottery that have the colors I would like to use. I don't expect all of them to be in the design.

I also put our logo file here and a pic of our current business card.

```html
<!DOCTYPE html>
<html lang="en">
<head>
<meta charset="utf-8">
<title>Redstone Valley Medical Group – Sign</title>
<link rel="stylesheet" href="https://fonts.googleapis.com/css2?family=Oswald:wght@700&display=swap">
<style>
  :root {
    --backdrop: #b9ccd2;
    --gold: #f9b03c;
    --maroon: #7d1a1c;
    --red: #c8232a;
    --coral: #ec5a3a;
    --orange: #f2682a;
    --teal: #27b3b0;
    --blue: #3b4fb8;
  }
  html, body {
    margin: 0;
    padding: 0;
    width: 1200px;
    height: 881px;
    overflow: hidden;
    background: var(--backdrop);
  }
  .canvas {
    position: relative;
    width: 1200px;
    height: 881px;
  }
  .sign {
    position: absolute;
    left: 352px;
    top: 192px;
    width: 496px;
    height: 496px;
    overflow: hidden;
  }
  .sign__pattern {
    position: absolute;
    inset: 0;
    background: linear-gradient(90deg,
      var(--red) 0%, #d9454f 14%, var(--coral) 30%,
      var(--orange) 45%, var(--teal) 58%, var(--coral) 68%,
      var(--orange) 76%, var(--blue) 86%, var(--teal) 93%, var(--blue) 100%);
  }
  .sign__badge {
    position: absolute;
    left: 68px;
    top: 25px;
    width: 360px;
    height: 360px;
    border-radius: 50%;
    background: var(--gold);
    display: flex;
    flex-direction: column;
    align-items: center;
    justify-content: center;
  }
  .sign__name {
    margin: 0;
    font-family: "Oswald", sans-serif;
    font-weight: 700;
    font-size: 44px;
    line-height: 1.15;
    letter-spacing: 1px;
    text-transform: uppercase;
    text-align: center;
    color: var(--maroon);
  }
  .sign__banner {
    position: absolute;
    left: 49px;
    top: 418px;
    width: 391px;
    height: 54px;
    box-sizing: border-box;
    border: 1px solid var(--maroon);
    background: var(--gold);
    display: flex;
    align-items: center;
    justify-content: center;
  }
  .sign__tagline {
    margin: 0;
    font-family: "Oswald", sans-serif;
    font-weight: 700;
    font-size: 27px;
    letter-spacing: 1px;
    text-transform: uppercase;
    color: var(--maroon);
  }
</style>
</head>
<body>
  <main class="canvas">
    <section class="sign">
      <div class="sign__pattern" role="img" aria-label="Streaked painterly background in red, coral, orange, teal and blue vertical bands"></div>
      <div class="sign__badge">
        <h1 class="sign__name">Redstone Valley<br>Medical Group</h1>
      </div>
      <div class="sign__banner">
        <p class="sign__tagline">The Wellness Lodge</p>
      </div>
    </section>
  </main>
</body>
</html>
```